Poster needed for hilariously funny interactive FARCE!!

Buried Beneath the Foam is a hilarious interactive murder mystery that takes place in a coffeehouse and bookstore called “Café Pinwheel.” The crazy cast of characters leads the audience through a maze of funny twists and turns. Opportunities for audience and cast interaction reach a peak when the audience is allowed to vote on the ending that they want to hear! There are four possible killers and four possible endings!
Updates

Hello Designers, I am trying to get SKETCHNOOKLY to extend the time of this project. Thanks for your patience. NTP

Target Market(s)

Community and professional Theatres as well as amateur theatre groups

Industry/Entity Type

Cafe

Requirements
Must have
• It must have the title and credit.
• BURIED BENEATH THE FOAM by Ned Parrow
• 'Hilariously funny interactive Murder Mystery'
Nice to have
• The show deals with a coffee shop called 'Cafe Pinwheel' and murder! It is a farce so it should relay that message through the poster.
Should not have
• Photos or images from movies..

```html
<!DOCTYPE html>
<html lang="en">
<head>
<meta charset="utf-8">
<title>Buried Beneath the Foam</title>
<link rel="stylesheet" href="https://fonts.googleapis.com/css2?family=Bagel+Fat+One&family=Bebas+Neue&display=swap">
<style>
  :root {
    --poster-blue: #0099db;
    --ink-white: #ffffff;
  }
  * { margin: 0; padding: 0; box-sizing: border-box; }
  html, body {
    width: 849px;
    height: 1200px;
    overflow: hidden;
    background: var(--poster-blue);
  }
  .poster {
    position: relative;
    width: 849px;
    height: 1200px;
    background: var(--poster-blue);
    color: var(--ink-white);
  }
  .title {
    position: absolute;
    top: 127px;
    left: 0;
    width: 100%;
    text-align: center;
    font-family: "Bagel Fat One", "Chewy", cursive;
    font-weight: 400;
    line-height: 1;
  }
  .title-line {
    display: block;
    white-space: nowrap;
    letter-spacing: -0.02em;
  }
  .title-line--buried  { font-size: 165px; }
  .title-line--beneath { font-size: 145px; margin-top: 38px; }
  .title-line--the     { font-size: 180px; margin-top: 32px; }
  .title-line--foam    { font-size: 240px; margin-top: 17px; }
  .tagline,
  .credit {
    position: absolute;
    left: 0;
    width: 100%;
    text-align: center;
    font-family: "Bebas Neue", "Oswald", sans-serif;
    font-weight: 400;
    font-size: 17px;
    line-height: 1.15;
    letter-spacing: 0;
  }
  .tagline { top: 1012px; }
  .credit  { top: 1068px; }
</style>
</head>
<body>
  <main class="poster">
    <h1 class="title" aria-label="Buried Beneath the Foam">
      <span class="title-line title-line--buried">BURIED</span>
      <span class="title-line title-line--beneath">BENEATH</span>
      <span class="title-line title-line--the">THE</span>
      <span class="title-line title-line--foam">FOAM</span>
    </h1>
    <p class="tagline">
      Buried Beneath the Foam is a hilarious interactive murder mystery that takes place in a<br>
      coffeehouse and bookstore called “Café Pinwheel.”
    </p>
    <p class="credit">by Ned Parrow</p>
  </main>
</body>
</html>
```